Brindle Logistics Business Card Design

We are a trucking and warehousing company. We run freight in the US manly from the Pacific NW to TX and back up the the PNW. We also do warehousing where we store, move, and distribute freight. Looking for a clean and modern design of business card. We would like to look rich and elegant. Attached is our logo.

Industry/Entity Type

Trucking Company

Contact Information for Business Card

Looking for a clean and modern design of business card. We would like to look rich and elegant.

Font styles to use
Sans Serif

Colors

Designer to choose colors to be used in the design.

Requirements
Must have
• logo but it should not dominate the card
Should not have
• logo should not dominate the card

```html
<!DOCTYPE html>
<html lang="en">
<head>
<meta charset="utf-8">
<title>Brindle Logistics Business Card</title>
<link href="https://fonts.googleapis.com/css2?family=Lato:wght@400;700;900&display=swap" rel="stylesheet">
<style>
  :root {
    --stage: #2a2a2c;
    --brand-blue: #1f6dbf;
    --brand-blue-light: #3b80cc;
    --card-white: #ececec;
    --ink: #2b2b2b;
    --ink-soft: #555;
    --white: #ffffff;
  }
  * { box-sizing: border-box; margin: 0; padding: 0; }
  html, body { width: 1200px; height: 800px; overflow: hidden; }
  body {
    background: var(--stage);
    font-family: "Lato", sans-serif;
    display: flex;
    align-items: center;
    justify-content: center;
    gap: 48px;
  }
  .card {
    width: 540px;
    height: 309px;
    position: relative;
    overflow: hidden;
    border-radius: 2px;
  }

  /* Front */
  .card-front { background: var(--brand-blue); color: var(--white); }
  .front-pattern {
    position: absolute; inset: 0;
    background: radial-gradient(circle at 40% 40%, var(--brand-blue-light), var(--brand-blue) 75%);
  }
  .front-brand {
    position: absolute; left: 60px; right: 60px; top: 118px;
    display: flex; align-items: center; justify-content: center; gap: 12px;
  }
  .brand-dot {
    flex: none;
    width: 22px; height: 22px; border-radius: 50%;
    background: var(--white);
  }
  .front-name {
    font-size: 28px; font-weight: 900; letter-spacing: 1.5px;
    text-transform: uppercase; color: var(--white); white-space: nowrap;
  }
  .front-web {
    position: absolute; left: 0; right: 0; bottom: 44px;
    text-align: center; font-size: 13px; color: var(--white);
  }
  .front-web strong { font-weight: 700; }

  /* Back */
  .card-back { background: var(--card-white); color: var(--ink); }
  .back-brand {
    position: absolute; top: 46px; left: 0; right: 0;
    display: flex; align-items: center; justify-content: center; gap: 10px;
  }
  .back-brand .brand-dot { width: 18px; height: 18px; background: var(--brand-blue); }
  .back-name {
    font-size: 22px; font-weight: 900; letter-spacing: 1.5px;
    text-transform: uppercase; color: var(--brand-blue); white-space: nowrap;
  }
  .person { position: absolute; top: 110px; left: 0; right: 0; text-align: center; }
  .person-name {
    font-size: 19px; font-weight: 700; letter-spacing: 2px;
    text-transform: uppercase; color: var(--brand-blue);
  }
  .person-title { font-size: 13px; color: var(--ink-soft); margin-top: 4px; }

  .contacts {
    position: absolute; left: 16px; right: 16px; bottom: 38px;
    display: grid;
    grid-template-columns: 1fr 2px 0.8fr 2px 1.7fr;
    column-gap: 15px;
    align-items: start;
  }
  .contact {
    text-align: center; font-size: 12px; line-height: 1.45; color: var(--ink);
    white-space: nowrap;
  }
  .contact-icon {
    width: 24px; height: 24px; margin: 0 auto 8px; display: block;
  }
  .divider {
    width: 2px; height: 34px; margin-top: 34px;
    background: var(--brand-blue); transform: skewX(-18deg);
  }
</style>
</head>
<body>

  <section class="card card-front" aria-label="Card front">
    <div class="front-pattern" role="img" aria-label="Faint repeating brand pattern on blue"></div>
    <div class="front-brand">
      <span class="brand-dot"></span>
      <span class="front-name">Brindle Logistics, LLC</span>
    </div>
    <p class="front-web">www.<strong>brindlelogisticsllc</strong>.com</p>
  </section>

  <section class="card card-back" aria-label="Card back">
    <div class="back-brand">
      <span class="brand-dot"></span>
      <span class="back-name">Brindle Logistics, LLC</span>
    </div>

    <div class="person">
      <p class="person-name">Daniel Morrow</p>
      <p class="person-title">Managing Director</p>
    </div>

    <div class="contacts">
      <div class="contact contact-address">
        <svg class="contact-icon" viewBox="0 0 24 24" fill="none" stroke="var(--brand-blue)" stroke-width="1.4">
          <circle cx="12" cy="12" r="11"/>
          <path d="M12 18s-4-4.2-4-7.2a4 4 0 0 1 8 0c0 3-4 7.2-4 7.2z"/>
          <circle cx="12" cy="10.8" r="1.4"/>
        </svg>
        4218 NE 88th Avenue<br>Portland, OR 97220
      </div>
      <span class="divider"></span>
      <div class="contact contact-phone">
        <svg class="contact-icon" viewBox="0 0 24 24" fill="none" stroke="var(--brand-blue)" stroke-width="1.4">
          <circle cx="12" cy="12" r="11"/>
          <path d="M9 7l1.6 2.6-1.1 1.2a6 6 0 0 0 3.7 3.7l1.2-1.1L17 15l-1 1.8c-4.5 0-8.8-4.3-8.8-8.8z" stroke-linejoin="round"/>
        </svg>
        360-555-0140<br>360-555-0142
      </div>
      <span class="divider"></span>
      <div class="contact contact-web">
        <svg class="contact-icon" viewBox="0 0 24 24" fill="none" stroke="var(--brand-blue)" stroke-width="1.4">
          <circle cx="12" cy="12" r="11"/>
          <circle cx="12" cy="12" r="5.5"/>
          <path d="M6.5 12h11M12 6.5c-2.4 3-2.4 8 0 11M12 6.5c2.4 3 2.4 8 0 11"/>
        </svg>
        daniel@brindlelogisticsllc.com<br>www.brindlelogisticsllc.com
      </div>
    </div>
  </section>

</body>
</html>
```